Brochure for Structivo, will be used to hand out to clients.

Need a design for a company brochure (4 pages including front&back + 2 in the middle that looks professional and sells our engineering capabilities to prospective clients. These clients will be architects, builders and developers.

Instructions
1) Open the brochure concept design PDF documents
2) Refer to photo, word files and PDF add in's
3) Setup the Resume section with photo + description and bullet points which can be filled in later (I will advise in 1 or 2 revisions)

The "Services Integration" PDF graph needs a bit of work to tart it up a bit and then inserted into the noted area.

I consider what I have provided as a guideline (neat laid out doc) however you have the ability to change the design if you think it could be better. Must be 4 pages and contain majority of info I have provided.

Target Market(s)

Architects, developers, builders

Industry/Entity Type

Engineering Consultant

Font styles to use
Serif
Sans Serif

Colors
9bcb3b
abd036
cadf82
eaf2ce
86cfc7
cfeae6
fbf289
fee18a
fbc994

Requirements
Must have
• The Brochure should be 4 x A4 pages which is a printed A3 sheet and then folded in half into a neat document.
• Presents well
Nice to have
• Brochure to be professional, minimalistic in a way but also interesting.
• Company colors are in our logo which is predominately green. Will leave colour scheme to the designer

```html
<!DOCTYPE html>
<html lang="en">
<head>
<meta charset="utf-8">
<title>Structivo – Building Service Consultant Brochure</title>
<link href="https://fonts.googleapis.com/css2?family=Montserrat:wght@300;400;600;700;800&display=swap" rel="stylesheet">
<style>
:root{
  --green:#8cc63e;
  --green-dark:#6fa82a;
  --green-soft:#cadf82;
  --green-wash:#eaf2ce;
  --ink:#2b2b2b;
  --text:#3d3d3d;
  --stage:#6b6b6b;
  --paper:#ffffff;
  --badge-teal:#5fa9b0;
  --badge-grey:#c9ccce;
}
*{margin:0;padding:0;box-sizing:border-box}
html,body{width:918px;height:1200px;overflow:hidden}
body{background:var(--stage);font-family:'Montserrat',sans-serif;color:var(--text);position:relative}
.spread{position:absolute;left:20px;top:289px;width:878px;height:622px;background:var(--paper);overflow:hidden}
.page-left,.page-right{position:absolute;top:0;height:622px;width:439px;overflow:hidden}
.page-left{left:0;background:
  radial-gradient(ellipse 260px 70px at 120px 20px,var(--green-wash),transparent 80%),
  radial-gradient(ellipse 300px 60px at 220px 622px,var(--green-wash),transparent 80%),#fff}
.page-right{left:439px;background:
  radial-gradient(ellipse 340px 110px at 200px 590px,var(--green-wash),transparent 80%),
  linear-gradient(180deg,#fff 70%,#f4f9e8)}
.abs{position:absolute}

/* left page */
.team-ribbon{left:105px;top:10px;width:230px;height:23px;background:var(--green);color:#fff;font-weight:700;font-size:12.5px;line-height:23px;text-align:center;clip-path:polygon(0 0,100% 0,96% 100%,4% 100%)}
.member{position:absolute;top:50px;width:118px;text-align:center}
.portrait{width:64px;height:64px;border-radius:50%;margin:0 auto;border:2px solid #fff;box-shadow:0 1px 3px rgba(0,0,0,.3)}
.portrait.photo{background:radial-gradient(circle at 50% 40%,#b98f78,#3a3a3a 75%)}
.portrait.blank{background:#d4d6d8}
.member-name{color:var(--green-dark);font-weight:700;font-size:8.5px;margin-top:8px}
.member-role{font-size:5.6px;margin-top:2px;line-height:1.3}
.member-bio{font-size:5.1px;line-height:1.32;text-align:justify;margin-top:6px}
.sector-bar{position:absolute;left:24px;width:391px;height:15px;background:var(--green);color:#fff;font-weight:700;font-size:7.5px;letter-spacing:1.6px;text-align:center;line-height:15px}
.project-list{position:absolute;font-size:5.1px;line-height:7.1px;list-style:none}
.project-list li{display:flex}
.project-list .value{width:34px;flex:none}
.footer-brand{left:30px;top:560px;width:70px;text-align:center}
.brand-mark{width:26px;height:26px;border-radius:50%;background:var(--green);margin:0 auto 4px}
.brand-name{font-weight:700;color:var(--green-dark);font-size:9.5px;letter-spacing:.5px}
.contact{left:110px;top:565px;font-size:5.2px;line-height:7.6px;list-style:none}
.contact li{display:flex;align-items:center;gap:4px}
.contact svg{width:6px;height:6px;fill:var(--green)}
.badge{top:564px;width:34px;height:34px}
.badge.one{left:300px;background:var(--badge-teal);border-radius:4px}
.badge.two{left:366px;background:var(--badge-grey);border-radius:50%}

/* right page */
.photo-tile{position:absolute;border-radius:14px;overflow:hidden}
.tile-ducts{left:21px;top:19px;width:195px;height:186px;background:linear-gradient(135deg,#c9d2d8,#7d8a93 60%,#b8c2c8)}
.tile-switch{left:223px;top:19px;width:195px;height:186px;background:linear-gradient(120deg,#8a9298,#c4c9cc 50%,#6f777c)}
.tile-pumps{left:21px;top:213px;width:195px;height:189px;background:linear-gradient(160deg,#5f8fb8,#8f9ba3 50%,#4b5a63)}
.tile-pipes{left:223px;top:213px;width:195px;height:189px;background:linear-gradient(150deg,#d6d6d4,#a9aaa8 45%,#b23a30 55%,#c8c8c6 70%)}
.logo-box{left:146px;top:152px;width:148px;height:148px;background:#fff;display:flex;flex-direction:column;align-items:center;justify-content:center}
.logo-box .brand-mark{width:54px;height:54px;margin-bottom:12px}
.logo-box .brand-name{font-size:19px;color:var(--green-dark)}
.headline{left:22px;top:446px;text-transform:uppercase;line-height:1}
.headline .l1{display:block;font-weight:800;color:var(--green);font-size:38.5px;letter-spacing:.5px}
.headline .l2{display:block;font-weight:800;color:var(--green);font-size:50px;margin-top:3px;letter-spacing:.3px}
.headline .l3{display:block;font-weight:300;color:var(--ink);font-size:33px;margin-top:6px}
.service-tags{left:303px;top:444px;width:136px;list-style:none}
.service-tags li{position:relative;height:18px;margin-bottom:4px;padding-left:16px;color:#fff;font-weight:600;font-size:9.5px;line-height:18px}
.service-tags li.green{background:var(--green)}
.service-tags li.dark{background:var(--ink)}
.service-tags li.tall{height:32px;line-height:12px;padding-top:4px}
.service-tags svg{position:absolute;left:-4px;top:4px;width:11px;height:11px}
.website{left:150px;top:594px;width:260px;text-align:center;font-size:7.5px;letter-spacing:4px;color:var(--ink)}
</style>
</head>
<body>
<main class="spread">

  <section class="page-left">
    <div class="abs team-ribbon">OUR SENIOR DESIGN TEAM</div>

    <div class="member" style="left:21px">
      <div class="portrait photo" role="img" aria-label="Portrait photo of Peter Halvorsen"></div>
      <div class="member-name">PETER HALVORSEN</div>
      <div class="member-role">Mechanical Services Engineer</div>
      <p class="member-bio">Peter has over 12 years' experience within the building services field primarily as a design engineer. He has extensive expertise in concept design of major buildings, employing energy efficient and innovative technologies in all services and using his contracting experience to provide pragmatic workable solutions.</p>
    </div>
    <div class="member" style="left:157px">
      <div class="portrait photo" role="img" aria-label="Portrait photo of Martin Ashby"></div>
      <div class="member-name">MARTIN ASHBY</div>
      <div class="member-role">Hydraulic / Wet Fire<br>Service Engineer</div>
      <p class="member-bio">During the past 30 years Martin has gained extensive experience in many fields of Hydraulic and Fire Services covering design in Health, Aged Care, Commercial buildings, Retail, Industrial, Sporting Venues, Defence Installations, Residential developments and Shopping Centres.</p>
    </div>
    <div class="member" style="left:290px">
      <div class="portrait blank" role="img" aria-label="Placeholder portrait for team member"></div>
      <div class="member-name">NAME GOES HERE</div>
      <div class="member-role">Electrical Services Engineer</div>
      <p class="member-bio">Lorem Ipsum is simply dummy text of the printing and typesetting industry. Lorem Ipsum has been the industry's standard dummy text ever since the 1500s, when an unknown printer took a galley of type and scrambled it to make a type specimen book.</p>
    </div>

    <div class="sector-bar" style="top:231px">RESIDENTIAL</div>
    <ul class="project-list" style="left:27px;top:256px;width:380px">
      <li><span class="value">$200m</span>Elmswood Park Precinct residential development (8 levels) Old Quarry site</li>
      <li><span class="value">$16m</span>Hillcrest Housing Development (former poultry farm)</li>
      <li><span class="value">$35m</span>Regent Street residential (17 levels)</li>
      <li><span class="value">$70m</span>Larkspur Gardens residential development (8 levels)</li>
      <li><span class="value">$30m</span>Ashgrove Towers, residential unit complex upgrades (10 levels)</li>
      <li><span class="value">$100m</span>Hillcrest Terraces, residential unit complex upgrades (10 levels)</li>
      <li><span class="value">$20m</span>Diocese of Riverbend, accommodation for priests and trainee priests</li>
    </ul>

    <div class="sector-bar" style="top:310px">OFFICES</div>
    <ul class="project-list" style="left:27px;top:334px;width:380px">
      <li><span class="value">$250m</span>Ridgeway Station: Tarrow Plaza (retail, commercial &amp; 25 level residential)</li>
      <li><span class="value">$300m</span>Millbrook Street Dunmore (retail, commercial &amp; residential)</li>
      <li><span class="value">$140m</span>Queens Lane: The Solace (48 level residential &amp; retail)</li>
      <li><span class="value">$20m</span>18 Kestrel Road Fairhaven</li>
      <li><span class="value">$250m</span>Ridgeway Station: Tarrow Plaza (retail, commercial &amp; 25 level residential)</li>
      <li><span class="value">$300m</span>Millbrook Street Dunmore (retail, commercial &amp; residential)</li>
      <li><span class="value">$140m</span>Queens Lane: The Solace (48 level residential &amp; retail)</li>
      <li><span class="value">$20m</span>18 Kestrel Road Fairhaven</li>
    </ul>

    <div class="sector-bar" style="top:396px">RETAIL / INDUSTRIES</div>
    <ul class="project-list" style="left:27px;top:421px;width:190px">
      <li><span class="value">$10m</span>Harbourview: New Consulate</li>
      <li><span class="value">$10m</span>Westmoor: Consulate Annex</li>
      <li><span class="value">$5m</span>Gull Point Upgrades</li>
      <li><span class="value">$5m</span>Cape Orrin Upgrades</li>
      <li><span class="value">$5m</span>Tern Island Upgrades</li>
    </ul>
    <ul class="project-list" style="left:228px;top:421px;width:190px">
      <li><span class="value">$10m</span>Harbourview: New Consulate</li>
      <li><span class="value">$10m</span>Westmoor: Consulate Annex</li>
      <li><span class="value">$5m</span>Gull Point Upgrades</li>
      <li><span class="value">$5m</span>Cape Orrin Upgrades</li>
      <li><span class="value">$5m</span>Tern Island Upgrades</li>
    </ul>

    <div class="sector-bar" style="top:461px">HOSPITAL / MEDICAL</div>
    <ul class="project-list" style="left:27px;top:487px;width:190px">
      <li><span class="value">$10m</span>Northgate Hospital ward and kitchen upgrades</li>
      <li><span class="value">$10m</span>Ashvale Hospital wards upgrades</li>
      <li><span class="value">$200m</span>Fernleigh Hospital</li>
      <li><span class="value">$4m</span>Veridian Labs (medical): pharmaceutical laboratory development</li>
      <li><span class="value">$4m</span>Cardiomed: sleep research facilities, heart &amp; spinal equipment testing</li>
    </ul>
    <ul class="project-list" style="left:228px;top:487px;width:190px">
      <li><span class="value">$10m</span>Lakeside Private Hospital: two new Hybrid Operating Theatres</li>
      <li><span class="value">$10m</span>Brookfield Hospital: two new Hybrid Operating Theatres and first stage Recovery area</li>
      <li><span class="value">$30m</span>Harwell Hospital (New)</li>
      <li><span class="value">$30m</span>Oakridge Dental Clinic</li>
      <li><span class="value">$5m</span>Bayside Day Surgery</li>
      <li><span class="value">$5m</span>Sunbeam Children's Ward upgrade</li>
    </ul>

    <div class="abs footer-brand">
      <div class="brand-mark"></div>
      <div class="brand-name">STRUCTIVO</div>
    </div>
    <ul class="abs contact">
      <li><svg viewBox="0 0 10 10"><path d="M5 0a3.5 3.5 0 0 0-3.5 3.5C1.5 6 5 10 5 10s3.5-4 3.5-6.5A3.5 3.5 0 0 0 5 0z"/></svg>Unit 4, 12 Harlow Place,</li>
      <li style="padding-left:10px">Greenvale</li>
      <li><svg viewBox="0 0 10 10"><path d="M2 0l2 2.5-1.2 1.3a6 6 0 0 0 3.4 3.4L7.5 6 10 8l-1.5 2C4 10 0 6 0 1.5z"/></svg>0400 555 019</li>
      <li><svg viewBox="0 0 10 10"><path d="M0 2h10v6H0z"/></svg>info@structivo-eng.com</li>
      <li><svg viewBox="0 0 10 10"><circle cx="5" cy="5" r="5"/></svg>www.structivo-eng.com</li>
    </ul>
    <div class="abs badge one" role="img" aria-label="Energy rating partner badge"></div>
    <div class="abs badge two" role="img" aria-label="Professional membership badge"></div>
  </section>

  <section class="page-right">
    <div class="photo-tile tile-ducts" role="img" aria-label="Photo of rooftop ventilation ductwork"></div>
    <div class="photo-tile tile-switch" role="img" aria-label="Photo of electrical switchboard room"></div>
    <div class="photo-tile tile-pumps" role="img" aria-label="Photo of plant room pumps and pipework"></div>
    <div class="photo-tile tile-pipes" role="img" aria-label="Photo of red fire sprinkler pipes on ceiling"></div>
    <div class="abs logo-box">
      <div class="brand-mark"></div>
      <div class="brand-name">STRUCTIVO</div>
    </div>

    <h1 class="abs headline">
      <span class="l1">Building</span>
      <span class="l2">Service</span>
      <span class="l3">Consultant</span>
    </h1>

    <ul class="abs service-tags">
      <li class="green"><svg viewBox="0 0 12 12"><circle cx="6" cy="6" r="6" fill="#6fa82a"/><path d="M3 6.2l2 2 4-4.4" stroke="#fff" stroke-width="1.6" fill="none"/></svg>Mechanical</li>
      <li class="dark"><svg viewBox="0 0 12 12"><circle cx="6" cy="6" r="6" fill="#8cc63e"/><path d="M3 6.2l2 2 4-4.4" stroke="#fff" stroke-width="1.6" fill="none"/></svg>Electrical</li>
      <li class="green"><svg viewBox="0 0 12 12"><circle cx="6" cy="6" r="6" fill="#6fa82a"/><path d="M3 6.2l2 2 4-4.4" stroke="#fff" stroke-width="1.6" fill="none"/></svg>Hydraulic</li>
      <li class="dark"><svg viewBox="0 0 12 12"><circle cx="6" cy="6" r="6" fill="#8cc63e"/><path d="M3 6.2l2 2 4-4.4" stroke="#fff" stroke-width="1.6" fill="none"/></svg>Wet/Dry Fire</li>
      <li class="green tall"><svg viewBox="0 0 12 12"><circle cx="6" cy="6" r="6" fill="#6fa82a"/><path d="M3 6.2l2 2 4-4.4" stroke="#fff" stroke-width="1.6" fill="none"/></svg>Building Energy<br>Efficiency</li>
    </ul>

    <div class="abs website">www.structivo-eng.com</div>
  </section>

</main>
</body>
</html>
```